Small Artisan Bakery Needs a new Bread Bag Label

I'm looking for a new bread bag label design for our artisan bakery. I have attached photos of our current logo (we will be using this in the label) and pictures of our bread bag. For this project we will focus on one of our bread (100% Rye) however I would like the final final to be in a format I can edit for other bread types.

We are thinking that each bread bag will have 2 labels, our logo on top of the bread bag window (as shown in the attached photos) and simple bread description below the window.

We typically use Copperplate font however we are open to ideas as long as it keeps in alignment with our logo.

*Also note, we will not be printing the labels directly on the bag. The designs will be printed as labels that will be stuck on each bag. I would like to have the final designs formatted in a way that makes it simple to have printed at a standard printing shop.

The bag is 9.5" long, 5" wide.

The length fro the bottom of the bag window to the bottom of the bag is 2".

Top of the bag to top of the window is a little over 4".

Since these labels will be printed on label paper and manually stuck on the bag I would like them to not be take up up the whole space above or below the bag window. If the label design comes to the edge of the bag it will be very difficult to physically stick the label on the bag straight.

Thanks

Hi, The bag is 9.5" long, 5" wide. The length fro the bottom of the bag window to the bottom of the bag is 2". Top of the bag to top of the window is a little over 4". Since these labels will be printed on label paper and manually stuck on the bag I would like them to not be take up up the whole space above or below the bag window. If the label design comes to the edge of the bag it will be very difficult to physically stick the label on the bag straight. Thanks

```html
<!DOCTYPE html>
<html lang="en">
<head>
<meta charset="UTF-8">
<title>Willow Brook Bread – 100% Rye Bread Bag Labels</title>
<link rel="stylesheet" href="https://fonts.googleapis.com/css2?family=Cinzel:wght@600;700;800&display=swap">
<style>
  :root {
    --backdrop: #121414;
    --kraft: #f5cfa3;
    --fold-line: #e2bd93;
    --window-edge: #b39a86;
    --label-white: #ffffff;
    --rim-blue: #2b2bd6;
    --rim-red: #e8141a;
    --banner-red: #ef1a1a;
    --sun-core: #fff6a0;
    --sun-mid: #ffd21e;
    --sun-edge: #f59a12;
    --name-ink: #1b1712;
    --desc-orange: #ff8a10;
    --desc-red: #f0321a;
    --pill-yellow: #fff35a;
    --pill-pale: #fffbc8;
    --desc-blue: #1a1ad8;
  }
  * { box-sizing: border-box; margin: 0; padding: 0; }
  html, body {
    width: 900px; height: 1200px; overflow: hidden;
    background: var(--backdrop);
  }
  .canvas { position: relative; width: 900px; height: 1200px; }
  .bag {
    position: absolute; left: 157px; top: 37px;
    width: 589px; height: 1125px;
    background: var(--kraft);
  }
  .fold { position: absolute; left: 0; right: 0; height: 1px; background: var(--fold-line); }
  .fold--upper { top: 473px; }
  .fold--lower { top: 887px; }
  .bag-window {
    position: absolute; left: 115px; top: 473px;
    width: 362px; height: 414px;
    border: 1px solid var(--window-edge);
    border-radius: 56px;
  }
  .logo-label { position: absolute; left: 57px; top: 57px; width: 472px; height: 360px; }
  .logo-label svg { display: block; width: 100%; height: 100%; }
  .brand-name {
    font-family: "Cinzel", "Times New Roman", serif;
    font-weight: 700;
    fill: var(--name-ink);
    letter-spacing: 3px;
  }
  .product-title {
    font-family: "Cinzel", "Times New Roman", serif;
    font-weight: 800;
    fill: var(--label-white);
  }
  .description-label {
    position: absolute; left: 27px; top: 917px;
    width: 535px; height: 154px;
    background: radial-gradient(ellipse at 50% 45%, var(--desc-orange) 30%, var(--desc-red) 100%);
    text-align: center;
    font-family: "Cinzel", "Times New Roman", serif;
  }
  .trim {
    position: absolute; top: 0; bottom: 0; width: 30px;
    background: linear-gradient(180deg, #d8101a, #f03040 50%, #d8101a);
  }
  .trim--left { left: 0; }
  .trim--right { right: 0; }
  .method {
    padding-top: 19px;
    color: var(--label-white);
    font-weight: 700; font-size: 17px; line-height: 24px;
  }
  .ingredients {
    margin: 6px auto 0;
    width: 434px; height: 84px;
    border: 3px solid var(--label-white);
    border-radius: 42px;
    background: radial-gradient(ellipse at 50% 50%, var(--pill-pale) 10%, var(--pill-yellow) 70%);
    color: var(--desc-blue);
    font-weight: 700; font-size: 17px; line-height: 24px;
    display: flex; flex-direction: column; justify-content: center;
  }
</style>
</head>
<body>
<main class="canvas">
  <section class="bag">
    <div class="fold fold--upper"></div>
    <div class="fold fold--lower"></div>
    <div class="bag-window"></div>

    <div class="logo-label">
      <svg viewBox="0 0 472 360" xmlns="http://www.w3.org/2000/svg">
        <defs>
          <radialGradient id="sunburst" cx="50%" cy="48%" r="65%">
            <stop offset="0%" stop-color="#fff6a0"/>
            <stop offset="45%" stop-color="#ffd21e"/>
            <stop offset="100%" stop-color="#f59a12"/>
          </radialGradient>
        </defs>
        <path class="label-edge" d="M0,360 V200 A236,200 0 0 1 472,200 V360 Z" fill="var(--label-white)"/>
        <path class="rim-blue" d="M9,351 V202 A227,191 0 0 1 463,202 V351 Z" fill="var(--rim-blue)"/>
        <path class="rim-red" d="M13,347 V203 A223,187 0 0 1 459,203 V347 Z" fill="var(--rim-red)"/>
        <path class="sunburst" role="img" aria-label="Radiating yellow and orange sunburst behind the bakery name"
              d="M17,343 V204 A219,183 0 0 1 455,204 V343 Z" fill="url(#sunburst)"/>
        <text class="brand-name" x="236" y="140" text-anchor="middle" font-size="36">WILLOW BROOK</text>
        <text class="brand-name" x="236" y="190" text-anchor="middle" font-size="36">BREAD</text>
        <rect class="title-banner" x="13" y="272" width="446" height="75" fill="var(--rim-blue)"/>
        <rect x="16" y="275" width="440" height="69" fill="var(--banner-red)"/>
        <text class="product-title" x="236" y="327" text-anchor="middle" font-size="44">100% RYE BREAD</text>
      </svg>
    </div>

    <div class="description-label">
      <div class="trim trim--left" role="img" aria-label="Red decorative diamond border"></div>
      <div class="trim trim--right" role="img" aria-label="Red decorative diamond border"></div>
      <p class="method">NATURALLY LEAVENED AND FERMENTED<br>100% LITHUANIAN RYE BREAD.</p>
      <p class="ingredients">
        <span>100% ORGANIC RYE FLOUR,</span>
        <span>110YEAR OLD ORGANIC RYE CULTURE,</span>
        <span>AND GREY CELTIC SEA SALT</span>
      </p>
    </div>
  </section>
</main>
</body>
</html>
```